MediDesk 4.2 is web based clinic management software. We require 1 logo for the software product, login page design and landing page (patient queue) design. The design should include all elements required logo, icons , buttons and type faces. http://md2021.tralvonix.my/Default.aspxTest login : KQ417 password : 4826 Final output should be in psd for developer to convert to css for web application.

Number of Pages Required

1 page

Colors

Designer to choose colors to be used in the design.

Requirements
Must have
• Product Logo , icon, login page design, and 1 main page design as attached.

```html
<!DOCTYPE html>
<html lang="en">
<head>
<meta charset="utf-8">
<title>MediDesk 4.2 — Login and Queue</title>
<link href="https://fonts.googleapis.com/css2?family=Hind:wght@300;400;500;600&display=swap" rel="stylesheet">
<style>
:root{
  --navy:#0a5aa0;
  --sky:#1591d6;
  --sky-btn:#0f95d8;
  --green:#6aab12;
  --red:#e53a2b;
  --orange:#f39a1e;
  --page:#f8f8f8;
  --panel:#f3f3f3;
  --white:#ffffff;
  --line:#d6d6d6;
  --ink:#222222;
  --muted:#666666;
}
*{box-sizing:border-box;margin:0;padding:0}
html,body{width:1200px;height:1200px;overflow:hidden}
body{position:relative;background:var(--page);font-family:"Hind",sans-serif;color:var(--ink)}
.abs{position:absolute}

.section-tag{position:absolute;left:0;color:var(--white);font-weight:400;display:flex;align-items:center;padding-left:17px;font-size:19px}
.section-tag--login{top:0;width:137px;height:45px;background:var(--navy)}
.section-tag--landing{top:632px;width:249px;height:45px;background:var(--sky);padding-left:22px}

.brand{position:absolute;left:0;width:1200px;top:118px;display:flex;justify-content:center;align-items:center;gap:14px}
.brand__dot{width:22px;height:22px;border-radius:50%;background:var(--sky)}
.brand__name{font-size:58px;font-weight:500;color:var(--navy);letter-spacing:-0.5px}

.login-card{position:absolute;left:296px;top:226px;width:624px;height:366px;background:var(--white);box-shadow:0 1px 3px rgba(0,0,0,.12)}
.field-label{position:absolute;left:72px;font-size:11px;color:var(--ink)}
.field-input{position:absolute;left:72px;width:480px;height:35px;border:1px solid #c9c9c9;background:var(--white)}
.link-clear{position:absolute;left:73px;top:262px;font-size:11px;color:var(--sky)}
.btn{position:absolute;color:var(--white);font-size:11.5px;display:flex;align-items:center;justify-content:center;gap:12px}
.btn--signup{left:313px;top:247px;width:75px;height:42px;background:var(--sky-btn)}
.btn--login{left:396px;top:247px;width:156px;height:42px;background:var(--navy)}

.screen{position:absolute;top:678px;width:600px;height:522px;overflow:hidden;background:var(--panel)}
.screen--home{left:0}
.screen--menu{left:600px}
.topbar{position:absolute;left:0;top:0;width:600px;height:40px;background:var(--navy)}
.topbar__menu{position:absolute;left:16px;top:15px}
.topbar__title{position:absolute;left:34px;top:12px;color:var(--white);font-size:9px;font-weight:500}
.topbar__logout{position:absolute;left:546px;top:11px;width:38px;height:17px;background:var(--red);color:var(--white);font-size:5px;display:flex;align-items:center;justify-content:center}

.card{position:absolute;background:var(--white);border-left:3px solid var(--sky)}
.date-card{left:60px;top:80px;width:170px;height:43px}
.date-card__icon{position:absolute;left:15px;top:14px;width:16px;height:16px;border-radius:50%;background:var(--sky)}
.date-card__time{position:absolute;left:39px;top:11px;font-size:9.5px;color:var(--navy)}
.date-card__sub{position:absolute;left:39px;top:27px;font-size:5px}

.filter{position:absolute;top:97px;font-size:5px;color:var(--ink)}
.filter__box{position:absolute;left:379px;top:97px;width:6px;height:6px;border:1px solid #bbb}
.select{position:absolute;left:474px;top:94px;width:65px;height:16px;border:1px solid #ccc;background:var(--white);font-size:5px;padding:5px 0 0 6px}
.select svg{position:absolute;right:5px;top:5px}

.queue-card{left:60px;top:140px;width:479px;height:136px}
.queue-card__title{position:absolute;left:19px;top:17px;font-size:9.5px;font-weight:500;color:var(--green)}
.queue-card__sub{position:absolute;left:19px;top:33px;font-size:5px}
.queue-card__sub em{font-style:normal;color:var(--orange)}
.btn-new{position:absolute;left:405px;top:17px;width:53px;height:16px;background:var(--green);color:var(--white);font-size:5px;display:flex;align-items:center;justify-content:center;gap:3px}
.thead,.trow span{position:absolute;font-size:5px;white-space:nowrap}
.thead{top:55px}
.table-box{position:absolute;left:19px;top:67px;width:436px;height:41px;border:1px solid var(--line);overflow:hidden}
.trow{position:absolute;left:0;top:0;width:434px;height:20px;background:#f7f7f7;border-bottom:1px solid var(--line)}
.trow span{top:7px}
.trow .amt em{font-style:normal;color:var(--orange)}
.pager{position:absolute;top:115px;font-size:5px;color:var(--muted)}

.footer{position:absolute;left:0;top:382px;width:600px;height:140px;background:var(--navy);color:var(--white)}
.footer__head{position:absolute;top:22px;font-size:9px}
.footer__text{position:absolute;left:59px;font-size:4.8px;line-height:6.6px}
.footer__links{position:absolute;right:60px;top:45px;text-align:right;font-size:4.8px;line-height:9.6px}

.scrim{position:absolute;left:0;top:0;width:600px;height:522px;background:rgba(0,0,0,.3)}
.drawer{position:absolute;left:600px;top:678px;width:140px;height:522px;background:var(--white)}
.drawer__avatar{position:absolute;left:19px;top:12px;width:36px;height:36px;border-radius:50%;background:radial-gradient(circle at 50% 40%,#8a8a8a,#2c2c2c)}
.drawer__name{position:absolute;left:66px;top:22px;font-size:7.5px;color:var(--navy)}
.drawer__id{position:absolute;left:66px;top:32px;font-size:4px;color:var(--orange)}
.drawer__rule{position:absolute;left:0;top:59px;width:140px;height:1px;background:#eeeeee}
.nav-item{position:absolute;left:24px;font-size:5px;display:flex;align-items:center;gap:7px}
.nav-item--active{color:var(--orange)}
.sub-list{position:absolute;left:20px;top:163px;list-style:none;font-size:5px;line-height:12px;color:#444}
</style>
</head>
<body>

<div class="section-tag section-tag--login">Login Screen</div>

<div class="brand">
  <span class="brand__dot"></span>
  <span class="brand__name">MediDesk</span>
</div>

<div class="login-card">
  <div class="field-label" style="top:80px">Username</div>
  <div class="field-input" style="top:102px"></div>
  <div class="field-label" style="top:157px">Password</div>
  <div class="field-input" style="top:180px"></div>
  <div class="link-clear">Clear</div>
  <div class="btn btn--signup">Sign Up</div>
  <div class="btn btn--login">Login to my account
    <svg width="8" height="12" viewBox="0 0 8 12"><path d="M1.5 1l5 5-5 5" fill="none" stroke="#fff" stroke-width="1.8"/></svg>
  </div>
</div>

<div class="section-tag section-tag--landing">Landing and Menu Screen</div>

<!-- Queue screen -->
<div class="screen screen--home">
  <div class="topbar">
    <svg class="topbar__menu" width="11" height="9" viewBox="0 0 11 9"><path d="M0 1h11M0 4.5h11M0 8h11" stroke="#fff" stroke-width="1.4"/></svg>
    <div class="topbar__title">MediDesk</div>
    <div class="topbar__logout">Logout</div>
  </div>
  <div class="card date-card">
    <div class="date-card__icon"></div>
    <div class="date-card__time">12:16 PM, OCTOBER 24 2018</div>
    <div class="date-card__sub">Queue Date - 10/24/2018</div>
  </div>
  <div class="filter__box"></div>
  <div class="filter" style="left:389px">Show all Status</div>
  <div class="filter" style="left:445px">Location</div>
  <div class="select">All Facilities<svg width="7" height="5" viewBox="0 0 7 5"><path d="M.5.5l3 3 3-3" fill="none" stroke="#555"/></svg></div>
  <div class="card queue-card">
    <div class="queue-card__title">Queue List</div>
    <div class="queue-card__sub">Listings of patiens in queue. <em>1</em> Result</div>
    <div class="btn-new">+ New Queue</div>
    <span class="thead" style="left:23px">No.</span>
    <span class="thead" style="left:98px">Patient Name</span>
    <span class="thead" style="left:185px">Time</span>
    <span class="thead" style="left:227px">Payor</span>
    <span class="thead" style="left:269px">Amount</span>
    <span class="thead" style="left:315px">Doctor</span>
    <span class="thead" style="left:357px">Location</span>
    <div class="table-box">
      <div class="trow">
        <span style="left:7px">1</span>
        <svg class="abs" style="left:26px;top:6px" width="30" height="7" viewBox="0 0 30 7"><circle cx="3" cy="2" r="1.6"/><path d="M0 7a3 3 0 0 1 6 0z"/><rect x="9" y="2" width="4" height="5"/><rect x="16" y="2" width="6" height="4"/><rect x="25" y="1" width="3.5" height="5"/></svg>
        <span style="left:75px">HALIM, SURAYA</span>
        <span style="left:124px">26 M</span>
        <span style="left:160px">9:00 AM</span>
        <span style="left:214px">-</span>
        <span class="amt" style="left:248px">RM <em>2,473</em></span>
        <span style="left:295px">000178</span>
        <span style="left:347px">-</span>
        <svg class="abs" style="left:375px;top:6px" width="50" height="7" viewBox="0 0 50 7" fill="none" stroke="#222" stroke-width=".9"><path d="M1 .5h4L1 6.5h4z"/><path d="M15 3.5a3 3 0 1 0 1-2.3M14 .5v2h2"/><rect x="29" y="1.5" width="4.5" height="4.5"/><path d="M32 4l3-3.5"/><circle cx="47" cy="2" r="1.5" fill="#222"/><path d="M44 7a3 3 0 0 1 6 0" fill="#222"/></svg>
      </div>
    </div>
    <div class="pager" style="left:26px">‹&nbsp;&nbsp;&nbsp;<span style="color:#222">Page 1 of 1</span>&nbsp;&nbsp;&nbsp;›</div>
    <div class="pager" style="left:398px">Rows per page:&nbsp;&nbsp;10&nbsp;&nbsp;⌄</div>
  </div>
  <div class="footer">
    <div class="footer__head" style="left:59px">Contact Us</div>
    <div class="footer__head" style="right:60px">Links</div>
    <div class="footer__text" style="top:45px">VORNEX SYSTEMS (MSC) SDN BHD<br>TRM VORNEX SYSTEMS SDN BHD</div>
    <div class="footer__text" style="top:65px">No. 214, Block C2, Jalan Meranti 3/7, Harbour Trade Park,<br>47300 Kelana Hills, Selangor, Malaysia</div>
    <div class="footer__text" style="top:85px">Tel. +603 5521 4068 , +6012 7730 418<br>Fax. 03 -5521 4069<br>Email : info@vornexsys.com</div>
    <div class="footer__text" style="top:115px">© 2018 Copyright MediDesk</div>
    <div class="footer__links">Home<br>Sign Up<br>Privacy Policy<br>Account</div>
  </div>
</div>

<!-- Menu open screen -->
<div class="screen screen--menu">
  <div class="topbar">
    <div class="topbar__title">MediDesk</div>
    <div class="topbar__logout">Logout</div>
  </div>
  <div class="card date-card">
    <div class="date-card__icon"></div>
    <div class="date-card__time">12:16 PM, OCTOBER 24 2018</div>
    <div class="date-card__sub">Queue Date - 10/24/2018</div>
  </div>
  <div class="filter__box"></div>
  <div class="filter" style="left:389px">Show all Status</div>
  <div class="filter" style="left:445px">Location</div>
  <div class="select">All Facilities<svg width="7" height="5" viewBox="0 0 7 5"><path d="M.5.5l3 3 3-3" fill="none" stroke="#555"/></svg></div>
  <div class="card queue-card">
    <div class="queue-card__sub">Listings of patiens in queue. <em>1</em> Result</div>
    <div class="btn-new">+ New Queue</div>
    <span class="thead" style="left:98px">Patient Name</span>
    <span class="thead" style="left:185px">Time</span>
    <span class="thead" style="left:227px">Payor</span>
    <span class="thead" style="left:269px">Amount</span>
    <span class="thead" style="left:315px">Doctor</span>
    <span class="thead" style="left:357px">Location</span>
    <div class="table-box">
      <div class="trow">
        <span style="left:75px">HALIM, SURAYA</span>
        <span style="left:124px">26 M</span>
        <span style="left:160px">9:00 AM</span>
        <span style="left:214px">-</span>
        <span class="amt" style="left:248px">RM <em>2,473</em></span>
        <span style="left:295px">000178</span>
        <span style="left:347px">-</span>
        <svg class="abs" style="left:375px;top:6px" width="50" height="7" viewBox="0 0 50 7" fill="none" stroke="#222" stroke-width=".9"><path d="M1 .5h4L1 6.5h4z"/><path d="M15 3.5a3 3 0 1 0 1-2.3M14 .5v2h2"/><rect x="29" y="1.5" width="4.5" height="4.5"/><path d="M32 4l3-3.5"/><circle cx="47" cy="2" r="1.5" fill="#222"/><path d="M44 7a3 3 0 0 1 6 0" fill="#222"/></svg>
      </div>
    </div>
    <div class="pager" style="left:398px">Rows per page:&nbsp;&nbsp;10&nbsp;&nbsp;⌄</div>
  </div>
  <div class="footer">
    <div class="footer__head" style="right:60px">Links</div>
    <div class="footer__text" style="top:65px">No. 214, Block C2, Jalan Meranti 3/7, Harbour Trade Park,<br>47300 Kelana Hills, Selangor, Malaysia</div>
    <div class="footer__links">Home<br>Sign Up<br>Privacy Policy<br>Account</div>
  </div>
  <div class="scrim"></div>
</div>

<nav class="drawer">
  <div class="drawer__avatar" role="img" aria-label="User profile photo"></div>
  <div class="drawer__name">Rafael Ostrander</div>
  <div class="drawer__id">KQ417</div>
  <div class="drawer__rule"></div>
  <div class="nav-item nav-item--active" style="top:78px"><svg width="7" height="6" viewBox="0 0 7 6" fill="#222"><rect y="0" width="7" height="1"/><rect y="2.5" width="7" height="1"/><rect y="5" width="7" height="1"/></svg>Queue</div>
  <div class="nav-item" style="top:97px"><svg width="8" height="6" viewBox="0 0 8 6" fill="#222"><circle cx="4" cy="1.5" r="1.5"/><path d="M1 6a3 3 0 0 1 6 0z"/></svg>Patient</div>
  <div class="nav-item" style="top:116px"><svg width="7" height="7" viewBox="0 0 7 7" fill="#222"><rect y="1" width="7" height="6"/></svg>Visit Entry</div>
  <div class="nav-item" style="top:135px"><svg width="8" height="6" viewBox="0 0 8 6" fill="#222"><rect width="8" height="6" rx="1"/></svg>Payment</div>
  <ul class="sub-list">
    <li>Claims Invoice</li><li>Standard</li><li>Auto-mode</li><li>Bulk</li><li>Flat</li><li>Maintenance</li><li>Clinic Information</li><li>Branch Information</li><li>Account</li><li>Logout</li>
  </ul>
</nav>

</body>
</html>
```